A Spinner Of Grace Company Brochure

I am the owner of a Mobile Disc Jockey company specializing in weddings. I am looking for a Tri Fold color brochure that is modern and eye catching with the focus being on upscale wedding events. I also want it to be easy to read and not overly cluttered ! I would like it to reflect our website located at aspinnerofgrace.example
I also have different variations and file types of my logo such as jpeg and png files. I need some good dance floor pics. If you do not have any good stock photos I can look through my photo library. I uploaded a logo and pic I found from one of my videos. Not sure if it is worth anything.
We also do Uplighting and Photo Booths which I would like in the brochure. Much of the text copy needed can be taken from our website if needed. Please refer to the website to see what we do and our style.

Target Market(s)

upscale weddings

Industry/Entity Type

wedding dj entertainment & masters of ceremonies

Requirements
Nice to have
• nice pictures of packed dance floors and people having fun

```html
<!DOCTYPE html>
<html lang="en">
<head>
<meta charset="utf-8">
<title>A Spinner Of Grace – Tri-Fold Brochure</title>
<link href="https://fonts.googleapis.com/css2?family=Roboto+Slab:wght@400;700;800&family=Montserrat:wght@400;500;600;700&display=swap" rel="stylesheet">
<style>
  :root{
    --purple:#8e3ea0;
    --purple-deep:#5b2168;
    --pink:#e0245e;
    --cream:#f8eee7;
    --ink:#2e2428;
    --grey:#6d6a6c;
    --white:#ffffff;
    --page:#e9e7e8;
  }
  *{box-sizing:border-box;margin:0;padding:0}
  html,body{width:1200px;height:1200px;overflow:hidden;background:var(--page)}
  body{font-family:"Montserrat",sans-serif;color:var(--ink);position:relative}
  .spread{position:absolute;left:20px;width:1160px;height:575px;background:var(--cream);overflow:hidden;box-shadow:0 4px 18px rgba(0,0,0,.18)}
  .spread.outside{top:20px}
  .spread.inside{top:605px;background:#fbf8f9}
  .fold{position:absolute;top:0;bottom:0;width:1px;background:rgba(0,0,0,.08);z-index:20}
  .abs{position:absolute}
  .photo{position:absolute}
  .ring{position:absolute;border-radius:50%;border:5px solid var(--purple);box-shadow:0 0 0 3px var(--white);z-index:6}
  .slab{font-family:"Roboto Slab",serif}
  .brand{font-family:"Roboto Slab",serif;font-weight:700;color:var(--grey);display:flex;align-items:center;gap:8px;white-space:nowrap}
  .brand .dot{width:14px;height:14px;border-radius:50%;background:var(--purple)}
  .body-copy{font-size:9.6px;line-height:1.5;color:var(--ink)}
  .body-copy p+p{margin-top:7px}
  .pink{color:var(--pink)}
  .purple{color:var(--purple)}

  /* outside: left flap */
  .flap-photo{left:0;top:0;width:387px;height:180px;background:linear-gradient(180deg,#d7b08a 0%,#b98772 45%,#e9d9d2 80%,var(--cream) 100%)}
  .flap-title{left:26px;top:190px;width:340px;font-size:21px;font-weight:800;line-height:1.1;text-transform:uppercase}
  .flap-tagline{left:26px;top:244px;width:340px;font-size:11.5px;font-weight:700;font-style:italic;color:var(--purple);line-height:1.35}
  .flap-copy{left:26px;top:284px;width:340px;font-size:9px;line-height:1.45}
  .flap-copy .narrow{width:220px}
  .owner-photo{right:8px;bottom:0;width:130px;height:150px;border-radius:65px 65px 0 0;background:linear-gradient(180deg,#c99a83 0%,#8f8f94 55%,#e9e6e6 100%)}
  .signature{left:40px;top:508px;width:130px;height:32px;background:linear-gradient(90deg,rgba(46,36,40,.12),rgba(46,36,40,.04));border-radius:4px}
  .owner-role{left:40px;top:548px;font-size:11px;font-weight:600}

  /* outside: back & cover */
  .outer-art{left:387px;top:0;width:773px;height:575px}
  .back-brand{left:420px;top:392px;font-size:24px}
  .contact-pill{left:505px;top:436px;background:var(--purple);color:var(--white);font-family:"Roboto Slab",serif;font-weight:700;font-size:12px;padding:5px 20px;border-radius:14px}
  .contacts{left:420px;top:478px;display:grid;grid-template-columns:150px 180px;row-gap:8px;column-gap:10px;font-size:9.5px}
  .contacts span{display:flex;align-items:center;gap:5px}
  .contacts svg{flex:none}
  .cover-brand{left:830px;top:24px;font-size:22px;z-index:4}
  .cover-head{left:885px;top:372px;width:265px;text-align:center;color:var(--white);z-index:4}
  .cover-head h1{font-family:"Roboto Slab",serif;font-weight:800;font-size:22px;line-height:1.12;text-transform:uppercase}
  .cover-head p{font-family:"Roboto Slab",serif;font-weight:700;font-size:11.5px;line-height:1.35;margin-top:10px}
  .cover-head .url{font-family:"Montserrat",sans-serif;font-weight:600;font-size:10px;margin-top:10px}

  /* inside */
  .in-left-photo{left:0;top:0;width:387px;height:255px;background:linear-gradient(180deg,#2a2430 0%,#4b3b45 40%,#8a6f6c 70%,#fbf8f9 100%)}
  .in-top-photo{left:387px;top:0;width:773px;height:250px;background:linear-gradient(180deg,#6c1f6a 0%,#b338a8 45%,#d9a6d4 78%,#fbf8f9 100%)}
  .in-title{left:24px;top:264px;width:350px;font-family:"Roboto Slab",serif;font-weight:800;font-size:15.5px;line-height:1.15;text-transform:uppercase}
  .in-sub{left:24px;top:324px;width:340px;font-family:"Roboto Slab",serif;font-weight:700;font-size:12px;color:var(--purple);line-height:1.3}
  .in-copy{left:24px;top:350px;width:340px}
  .services{width:330px}
  .service+.service{margin-top:14px}
  .service h3{font-family:"Roboto Slab",serif;font-weight:800;font-size:13px;color:var(--purple);text-transform:uppercase;letter-spacing:.2px}
  .service p{font-size:9.8px;line-height:1.5;margin-top:3px}
  .services.mid{left:414px;top:275px}
  .services.right{left:800px;top:255px}
  .cta{left:800px;top:390px;width:200px;font-family:"Roboto Slab",serif;font-weight:700;font-size:12px;line-height:1.3;color:var(--purple)}
  .cta strong{color:var(--pink)}
  .cta .call{display:block;margin-top:8px;color:var(--pink);font-size:14px;font-weight:800}
  .cta .call b{display:block;color:var(--ink);font-size:14px}
  .bouquet-photo{right:0;bottom:0;width:145px;height:200px;background:radial-gradient(ellipse at 55% 70%,#f4f2e8 0%,#dfe6d6 35%,#e6e9ef 70%,#fbf8f9 100%)}
</style>
</head>
<body>

<!-- OUTSIDE SPREAD -->
<section class="spread outside" aria-label="Brochure outside spread">
  <div class="fold" style="left:387px"></div>
  <div class="fold" style="left:773px"></div>

  <!-- inside flap -->
  <div class="photo flap-photo" role="img" aria-label="Couple sharing a first dance on a fog-covered ballroom floor"></div>
  <h2 class="abs flap-title slab"><span class="pink">Packing</span> Dance Floors<br>Since 1981!</h2>
  <div class="abs flap-tagline">Modern – Elegant – Attention to Detail –<br>Personalized – Fun</div>
  <div class="abs flap-copy body-copy">
    <p>A Spinner Of Grace is a professional wedding DJ, lighting &amp; photobooth company operating out of Cape Harbor, Florida and serving the Palm Bay, Cape Harbor, Coral Key, Seagrove &amp; Pelican Islands and surrounding areas. We bring a wealth of expertise, fun and knowledge to every celebration &amp; constantly exceed our client's expectations. Our talented team of DJs and MCs are passionate about making your event an unforgettable party.</p>
    <p class="narrow">We know how much work goes into planning a wedding or the simplest event so we've created a simple process to make planning your wedding or event easy, fun &amp; stress free! For weddings everything from your ceremony to the end of your reception will be crafted your way for an experience your guests will be talking about for years to come.</p>
  </div>
  <div class="photo owner-photo" role="img" aria-label="Portrait of the owner in a vest holding a microphone"></div>
  <div class="abs signature" role="img" aria-label="Owner's handwritten signature, Ray Morrow"></div>
  <div class="abs owner-role">Owner and Dj</div>

  <!-- back panel + cover art -->
  <svg class="abs outer-art" viewBox="0 0 773 575" aria-hidden="true">
    <defs>
      <linearGradient id="partyTone" x1="0" y1="0" x2="1" y2="1">
        <stop offset="0" stop-color="#d23fc0"/>
        <stop offset=".45" stop-color="#7d2b6d"/>
        <stop offset="1" stop-color="#3b2230"/>
      </linearGradient>
    </defs>
    <path d="M0,0 H773 V430 H560 C470,400 420,330 330,318 C230,305 110,330 0,300 Z" fill="url(#partyTone)" role="img" aria-label="Bride and guests dancing on a packed dance floor under pink uplighting"/>
    <path d="M387,0 H773 V62 C650,98 500,104 387,86 Z" fill="var(--cream)"/>
    <path d="M773,312 C590,312 430,395 412,575 H773 Z" fill="var(--white)"/>
    <path d="M773,324 C600,324 448,402 428,575 H773 Z" fill="var(--purple)"/>
  </svg>
  <div class="ring" style="left:400px;top:12px;width:120px;height:110px;background:linear-gradient(135deg,#7c5c8f,#2f2a3a)" role="img" aria-label="Guests posing with props in the photo booth"></div>
  <div class="ring" style="left:470px;top:215px;width:140px;height:140px;background:linear-gradient(135deg,#5a4552,#c9a7a9)" role="img" aria-label="Bride laughing with guests on the dance floor"></div>

  <div class="abs brand back-brand"><span class="dot"></span>A Spinner Of Grace</div>
  <div class="abs contact-pill">CONTACT US</div>
  <div class="abs contacts">
    <span><svg width="10" height="10" viewBox="0 0 10 10"><circle cx="5" cy="5" r="5" fill="var(--purple)"/><path d="M5 2a2 2 0 0 0-2 2c0 1.5 2 4 2 4s2-2.5 2-4a2 2 0 0 0-2-2z" fill="#fff"/></svg>Cape Harbor, FL 33900</span>
    <span><svg width="10" height="10" viewBox="0 0 10 10"><circle cx="5" cy="5" r="5" fill="var(--purple)"/><rect x="2.4" y="3" width="5.2" height="4" fill="#fff"/><path d="M2.4 3l2.6 2 2.6-2" stroke="var(--purple)" stroke-width=".7" fill="none"/></svg>ray@aspinnerofgrace.example</span>
    <span><svg width="10" height="10" viewBox="0 0 10 10"><circle cx="5" cy="5" r="5" fill="var(--purple)"/><path d="M3 2.6l1 1-.6.8c.4.8 1 1.4 1.8 1.8l.8-.6 1 1-.7.9C4.6 7.3 2.7 5.4 2.5 3.3z" fill="#fff"/></svg>239.555.0148</span>
    <span><svg width="10" height="10" viewBox="0 0 10 10"><circle cx="5" cy="5" r="5" fill="var(--purple)"/><circle cx="5" cy="5" r="2.6" fill="none" stroke="#fff" stroke-width=".8"/><path d="M2.4 5h5.2M5 2.4v5.2" stroke="#fff" stroke-width=".6"/></svg>www.aspinnerofgrace.example</span>
  </div>

  <div class="abs brand cover-brand"><span class="dot"></span>A Spinner Of Grace</div>
  <div class="abs cover-head">
    <h1>Modern,<br>Tasteful &amp; Fun<br>Entertainment</h1>
    <p>Weddings, Corporate Events,<br>Private Parties, any event<br>is better with A Spinner Of Grace</p>
    <div class="url">www.aspinnerofgrace.example</div>
  </div>
</section>

<!-- INSIDE SPREAD -->
<section class="spread inside" aria-label="Brochure inside spread">
  <div class="fold" style="left:387px"></div>
  <div class="fold" style="left:773px"></div>

  <div class="photo in-left-photo" role="img" aria-label="Newlyweds walking through a confetti send-off with cheering guests"></div>
  <div class="photo in-top-photo" role="img" aria-label="Couple dancing on clouds in a magenta-lit ballroom"></div>
  <div class="ring" style="left:24px;top:148px;width:100px;height:100px;background:linear-gradient(135deg,#7fb3c7,#d9c7b8)" role="img" aria-label="Bride and groom celebrating outdoors by the pool"></div>
  <div class="ring" style="left:280px;top:128px;width:112px;height:112px;background:linear-gradient(135deg,#8aa6d6,#c88a96)" role="img" aria-label="Guests singing together on the dance floor"></div>
  <div class="ring" style="left:400px;top:30px;width:115px;height:115px;background:linear-gradient(135deg,#c8356f,#3d2a3c)" role="img" aria-label="Groom lifted by friends during the reception"></div>

  <h2 class="abs in-title">Wedding Entertainment<br>Planning &amp; Coordination<br><span class="pink">The Way You Want It</span></h2>
  <div class="abs in-sub">How do you want your wedding remembered?</div>
  <div class="abs in-copy body-copy">
    <p>This is one of the first questions I ask couples when they contact us about wedding DJ entertainment and the response is always the same, <b>"I want a great party and everyone to leave saying it was the best wedding ever"!</b></p>
    <p>Beginning with your initial consultation, we listen to you and respond with creative ideas and helpful advice so your event <span class="pink">is all about you</span>. We know it's more than just great music, it's keeping you guests engaged and coordinating with your venue and vendors for a smooth and timely event everyone will never forget.</p>
    <p>Contact us now and find out why so many couples continue to place their faith and trust in us to help them create the ultimate wedding experience.</p>
  </div>

  <div class="abs services mid">
    <div class="service"><h3>Wedding Ceremonies</h3><p>We will be happy to provide your ceremony sound system, music and help you with the planning and organizational flow of your ceremony.</p></div>
    <div class="service"><h3>Dancing on Clouds</h3><p>Want to add that fairy tale romance that will "wow" your guests. Add our dancing on clouds option.</p></div>
    <div class="service"><h3>Lighting</h3><p>Uplighting can transform the atmosphere in your room from ordinary to extraordinary! When used with dance floor lighting it creates both energy and atmosphere.</p></div>
    <div class="service"><h3>Monogram Lighting</h3><p>Add more style! Let us put your name in lights. We offer over 20 different designs for you to choose from or we can create a custom design for you.</p></div>
  </div>

  <div class="abs services right">
    <div class="service"><h3>Photo Booth</h3><p>Add more fun and excitement to your event with our photo booth. We offer several back drops and props!</p></div>
    <div class="service"><h3>DJ Entertainment</h3><p>All of our team members are highly trained professional DJs and emcees with their own unique style.</p></div>
  </div>
  <div class="photo bouquet-photo" role="img" aria-label="White rose bridal bouquet with a couple in soft focus"></div>
  <div class="abs cta">
    <strong>Join Over 1,000 Happy Customers</strong> that have enjoyed A Spinner Of Grace<br>Have your event be remembered as being one of the greats!
    <span class="call">CALL TODAY<b>(239) 555-0148</b></span>
  </div>
</section>

</body>
</html>
```